Building/Renovation Company needs Website

I need a website designed for a renovation/building company based in Hampshire. We specialise in kitchens, bathrooms, carpentry, plastering, brickwork, ground/garden works and decorating, and all our work is fully insured and carried out to a high standard.

With the photos, display them in a before/after format.

Coded - Design and coding required

1 page

```html
<!DOCTYPE html>
<html lang="en">
<head>
<meta charset="utf-8">
<title>Hartwell Developments – Renovations across Hampshire</title>
<link href="https://fonts.googleapis.com/css2?family=Roboto:wght@400;500;700;900&display=swap" rel="stylesheet">
<style>
:root{
  --lime:#cfdc1f;
  --navy:#232a8c;
  --navy-deep:#1c2270;
  --ink:#1b1b1b;
  --text:#444;
  --white:#fff;
  --paper:#f4f4f4;
}
*{margin:0;padding:0;box-sizing:border-box}
html,body{width:1200px;height:4505px;overflow:hidden}
body{font-family:'Roboto',sans-serif;color:var(--ink);background:var(--white);position:relative}
.abs{position:absolute}
.placeholder{position:absolute}
.skew-btn{position:absolute;display:flex;align-items:center;justify-content:center;font-weight:500;font-size:15px;text-transform:uppercase;text-decoration:none;white-space:nowrap}
.skew-btn::before{content:"";position:absolute;inset:0;background:var(--lime);transform:skewX(-25deg);z-index:-1}
.skew-btn span{position:relative}

/* header */
.site-header{position:absolute;left:0;top:0;width:1200px;height:100px;background:var(--white);z-index:5}
.brand{position:absolute;left:112px;top:30px;display:flex;align-items:center;gap:10px}
.brand-mark{width:34px;height:34px;background:var(--lime)}
.brand-name{font-size:26px;font-weight:500;color:var(--navy);letter-spacing:1px}
.main-nav{position:absolute;left:446px;top:38px;display:flex;gap:26px;font-size:16px}
.main-nav a{color:var(--ink);text-decoration:none}
.main-nav a.active{color:var(--navy)}
.contact-btn{left:938px;top:27px;width:142px;height:42px;color:var(--navy-deep);z-index:1}

/* hero */
.hero{position:absolute;left:0;top:100px;width:1200px;height:625px;background:linear-gradient(160deg,#3b3f44 0%,#5a5148 45%,#8c7450 75%,#a58a5e 100%);clip-path:polygon(0 0,100% 0,100% 570px,0 625px)}
.hero-shade{position:absolute;inset:0;background:rgba(15,18,25,.45)}
.hero-frame{position:absolute;left:200px;top:207px;width:810px;height:326px}
.hero-frame .b{position:absolute;top:0;bottom:0;width:44px;border:4px solid var(--lime)}
.hero-frame .l{left:0;border-right:none}
.hero-frame .r{right:0;border-left:none}
.hero-title{position:absolute;left:0;top:252px;width:1200px;text-align:center;color:var(--white);font-size:47px;line-height:60px;font-weight:700}
.hero-lead{position:absolute;left:0;top:384px;width:1200px;text-align:center;color:var(--white);font-size:15px;line-height:22px}
.quote-btn{left:483px;top:448px;width:234px;height:44px;color:var(--navy-deep);z-index:1}
.scroll-arrow{position:absolute;left:581px;top:668px;width:38px;height:64px;background:var(--white);display:flex;align-items:center;justify-content:center;box-shadow:0 2px 6px rgba(0,0,0,.15)}

/* headings */
.section-mark{position:absolute;width:36px;height:36px;background:var(--lime)}
.section-title{position:absolute;left:0;width:1200px;text-align:center;font-size:36px;font-weight:700}

/* services */
.services-bg{position:absolute;left:0;top:700px;width:1200px;height:640px;background:linear-gradient(180deg,var(--paper),var(--white))}
.service-card{position:absolute;top:980px;width:233px;height:306px;background:var(--white);box-shadow:0 2px 8px rgba(0,0,0,.12)}
.service-card .photo{left:0;top:0;width:233px;height:248px}
.service-card .badge{position:absolute;left:92px;top:206px;width:50px;height:50px;background:var(--lime);display:flex;align-items:center;justify-content:center}
.service-card .label{position:absolute;left:0;top:248px;width:233px;height:58px;display:flex;align-items:center;justify-content:center;font-weight:700;font-size:16px;text-transform:uppercase}
.service-card.active .label{background:var(--navy);color:var(--white)}
.carousel-arrow{position:absolute;top:1087px;width:32px;height:32px;border:2px solid var(--ink);border-radius:50%;display:flex;align-items:center;justify-content:center}

/* about */
.about-photo{left:112px;top:1415px;width:532px;height:480px;background:linear-gradient(180deg,#9fa9b3 0%,#d9d9d6 40%,#7a6d5e 75%,#4a3f33 100%)}
.about-card{position:absolute;left:580px;top:1470px;width:508px;height:365px;background:var(--white);box-shadow:0 3px 14px rgba(0,0,0,.15)}
.about-card .section-mark{left:20px;top:36px}
.about-card h2{position:absolute;left:104px;top:38px;font-size:36px;font-weight:700}
.about-card p{position:absolute;left:104px;top:94px;width:360px;font-size:14px;line-height:24px;color:var(--text);text-align:justify}
.read-btn{left:110px;top:279px;width:140px;height:40px;color:var(--navy-deep);z-index:1}

/* why choose */
.why{position:absolute;left:0;top:2001px;width:1200px;height:749px;background:linear-gradient(160deg,#2a318f,#222a84)}
.why .section-mark{left:122px;top:60px}
.why h2{position:absolute;left:112px;top:168px;color:var(--white);font-size:36px;font-weight:700}
.why-item{position:absolute;left:112px;width:336px;height:114px}
.why-item + .why-item{border-top:1px solid rgba(255,255,255,.25)}
.why-item .icon{position:absolute;left:4px;top:20px;width:70px;height:70px;background:var(--lime);display:flex;align-items:center;justify-content:center}
.why-item h3{position:absolute;left:100px;top:36px;color:var(--white);font-size:16px;font-weight:700;text-transform:uppercase;white-space:nowrap}
.why-item p{position:absolute;left:100px;top:62px;color:#e4e6f5;font-size:14px;white-space:nowrap}
.why-frame{position:absolute;left:598px;top:2092px;width:440px;height:698px;border-left:3px solid var(--lime)}
.why-frame::before{content:"";position:absolute;left:-3px;top:0;width:442px;height:3px;background:var(--lime);transform-origin:left;transform:rotate(-4deg)}
.why-photo{left:620px;top:2065px;width:478px;height:741px;background:linear-gradient(180deg,#c7ccd4 0%,#e8e8e6 30%,#d7d8d8 75%,#4c4f55 100%);clip-path:polygon(0 30px,100% 0,100% 100%,0 100%)}

/* cta */
.cta-bg{left:0;top:2750px;width:1200px;height:560px;background:linear-gradient(180deg,#e8e6e2,#f7f6f3 70%,#fff)}
.cta-box{position:absolute;left:182px;top:2968px;width:836px;height:252px;background:var(--lime);border:2px solid var(--navy)}
.cta-box h2{position:absolute;left:0;top:66px;width:832px;text-align:center;font-size:36px;font-weight:700}
.cta-box p{position:absolute;left:100px;top:132px;width:632px;text-align:center;font-size:14px;line-height:23px;color:#333}
.cta-circle{position:absolute;left:552px;top:2914px;width:96px;height:96px;border-radius:50%;background:var(--white);display:flex;align-items:center;justify-content:center}
.cta-circle div{width:36px;height:36px;background:var(--lime)}
.cta-btn{left:492px;top:3197px;width:216px;height:42px;color:var(--white);z-index:1}
.cta-btn::before{background:var(--navy)}

/* before after */
.ba-photo{top:3555px;height:315px}
.ba-tag{position:absolute;bottom:14px;color:var(--white);font-size:22px;font-style:italic;font-weight:700}
.ba-nav{position:absolute;top:3915px;width:56px;height:40px;display:flex;align-items:center;justify-content:center;z-index:1}
.ba-nav::before{content:"";position:absolute;inset:0;transform:skewX(-25deg);z-index:-1}
.ba-nav.prev::before{background:var(--lime)}
.ba-nav.next::before{background:var(--navy)}

/* footer */
.site-footer{position:absolute;left:0;top:3990px;width:1200px;height:515px;background:linear-gradient(180deg,#1a1a1a,#101010);clip-path:polygon(0 80px,100% 0,100% 100%,0 100%)}
.footer-brand{position:absolute;left:0;top:4130px;width:1200px;display:flex;justify-content:center;align-items:center;gap:14px}
.footer-brand .brand-mark{width:48px;height:48px;background:var(--white)}
.footer-brand .brand-name{color:var(--white);font-size:38px}
.footer-nav{position:absolute;left:0;top:4268px;width:1200px;display:flex;justify-content:center;font-size:16px}
.footer-nav a{color:var(--white);text-decoration:none;padding:0 13px;border-left:1px solid rgba(255,255,255,.5)}
.footer-nav a:first-child{border-left:none}
.socials{position:absolute;left:0;top:4322px;width:1200px;display:flex;justify-content:center;gap:20px}
.socials span{width:36px;height:36px;border:2px solid var(--white);border-radius:50%}
.socials span.filled{background:var(--lime);border-color:var(--lime);border-radius:0}
.footer-rule{position:absolute;left:112px;top:4404px;width:976px;height:1px;background:rgba(255,255,255,.35)}
.to-top{position:absolute;left:1100px;top:4380px;width:36px;height:36px;background:var(--lime);display:flex;align-items:center;justify-content:center}
.copyright{position:absolute;left:0;top:4452px;width:1200px;text-align:center;color:var(--white);font-size:14px}
</style>
</head>
<body>

<header class="site-header">
  <div class="brand"><div class="brand-mark"></div><div class="brand-name">HARTWELL</div></div>
  <nav class="main-nav">
    <a class="active" href="#">HOME</a><a href="#">ABOUT US</a><a href="#">OUR SERVICES</a><a href="#">WHY CHOOSE US</a>
  </nav>
  <a class="skew-btn contact-btn"><span>Contact Us</span></a>
</header>

<section class="hero" role="img" aria-label="Photo of a newly built timber deck with balcony railing at dusk">
  <div class="hero-shade"></div>
</section>
<div class="hero-frame"><div class="b l"></div><div class="b r"></div></div>
<h1 class="hero-title">TRANSFORMING HOMES<br>WITH CRAFTSMANSHIP &amp; CARE</h1>
<p class="hero-lead">Renovations, building work, and bespoke improvements across Hampshire<br>delivered with precision, professionalism, and pride.</p>
<a class="skew-btn quote-btn"><span>Request a Free Quote</span></a>

<div class="services-bg"></div>
<div class="scroll-arrow"><svg width="16" height="34" viewBox="0 0 16 34"><path d="M8 2v28M2 23l6 8 6-8" stroke="#111" stroke-width="3" fill="none"/></svg></div>

<!-- services -->
<div class="section-mark" style="left:582px;top:812px"></div>
<h2 class="section-title" style="top:896px">OUR SERVICES</h2>
<div class="carousel-arrow" style="left:66px"><svg width="14" height="12" viewBox="0 0 14 12"><path d="M13 6H2M6 1L1 6l5 5" stroke="#111" stroke-width="1.8" fill="none"/></svg></div>
<div class="carousel-arrow" style="left:1102px"><svg width="14" height="12" viewBox="0 0 14 12"><path d="M1 6h11M8 1l5 5-5 5" stroke="#111" stroke-width="1.8" fill="none"/></svg></div>

<div class="service-card" style="left:112px">
  <div class="photo placeholder" role="img" aria-label="Photo of a modern kitchen with island and pendant lights" style="background:linear-gradient(180deg,#d8d2c8,#3a4150)"></div>
  <div class="badge"><svg width="28" height="28" viewBox="0 0 28 28" fill="none" stroke="#222" stroke-width="1.6"><rect x="3" y="12" width="22" height="13"/><path d="M3 18h22M14 12v13M8 4v8M20 4v8"/></svg></div>
  <div class="label">Kitchens</div>
</div>
<div class="service-card active" style="left:360px">
  <div class="photo placeholder" role="img" aria-label="Photo of a tiled bathroom with walk-in shower" style="background:linear-gradient(180deg,#cfcfcc,#5b5d60)"></div>
  <div class="badge"><svg width="28" height="28" viewBox="0 0 28 28" fill="none" stroke="#222" stroke-width="1.6"><path d="M6 25V6a3 3 0 016 0M4 14h20v4a6 6 0 01-6 6h-8a6 6 0 01-6-6z"/></svg></div>
  <div class="label">Bathrooms</div>
</div>
<div class="service-card" style="left:607px">
  <div class="photo placeholder" role="img" aria-label="Photo of a carpenter measuring timber in a workshop" style="background:linear-gradient(180deg,#6a5a48,#3a3128)"></div>
  <div class="badge"><svg width="28" height="28" viewBox="0 0 28 28" fill="none" stroke="#222" stroke-width="1.6"><path d="M4 24L18 10M14 6l8 8M20 4l4 4M6 6l16 16"/></svg></div>
  <div class="label">Carpentry</div>
</div>
<div class="service-card" style="left:855px">
  <div class="photo placeholder" role="img" aria-label="Photo of a plasterer smoothing a wall" style="background:linear-gradient(180deg,#c9c4bc,#4a5a8a)"></div>
  <div class="badge"><svg width="28" height="28" viewBox="0 0 28 28" fill="none" stroke="#222" stroke-width="1.6"><rect x="3" y="6" width="22" height="18"/><path d="M3 12h22M3 18h22M10 6v6M18 12v6M10 18v6"/></svg></div>
  <div class="label">Plastering</div>
</div>

<!-- about -->
<div class="placeholder about-photo" role="img" aria-label="Photo of a rendered terraced house rear with new patio"></div>
<div class="about-card">
  <div class="section-mark"></div>
  <h2>ABOUT US</h2>
  <p>Hartwell Developments is a trusted renovation and building company serving homeowners across Hampshire. From stunning kitchen and bathroom refurbishments to detailed carpentry, plastering, brickwork, and garden transformations, we deliver work that’s fully insured, carefully managed, and finished to the highest standard.</p>
  <a class="skew-btn read-btn"><span>Read More</span></a>
</div>

<!-- why choose -->
<section class="why">
  <div class="section-mark"></div>
  <h2>WHY CHOOSE US</h2>
</section>
<div class="why-item" style="top:2238px">
  <div class="icon"><svg width="36" height="36" viewBox="0 0 36 36" fill="none" stroke="#222" stroke-width="1.8"><path d="M18 4l11 4v9c0 7-5 12-11 15-6-3-11-8-11-15V8z"/><path d="M13 18l4 4 7-8"/></svg></div>
  <h3>Fully Insured &amp; Qualified</h3><p>Peace of mind from start to finish.</p>
</div>
<div class="why-item" style="top:2352px">
  <div class="icon"><svg width="36" height="36" viewBox="0 0 36 36" fill="none" stroke="#222" stroke-width="1.8"><circle cx="18" cy="18" r="6"/><path d="M18 4v5M18 27v5M4 18h5M27 18h5M8 8l4 4M24 24l4 4M8 28l4-4M24 12l4-4"/></svg></div>
  <h3>High-Standard Workmanship</h3><p>Attention to detail in every step.</p>
</div>
<div class="why-item" style="top:2466px">
  <div class="icon"><svg width="36" height="36" viewBox="0 0 36 36" fill="none" stroke="#222" stroke-width="1.8"><circle cx="11" cy="20" r="4"/><circle cx="25" cy="20" r="4"/><path d="M4 32c0-4 3-6 7-6s7 2 7 6M18 32c0-4 3-6 7-6s7 2 7 6M12 4h12v8h-8l-4 3z"/></svg></div>
  <h3>Clear Communication</h3><p>Transparent timelines and honest pricing.</p>
</div>
<div class="why-item" style="top:2580px">
  <div class="icon"><svg width="36" height="36" viewBox="0 0 36 36" fill="none" stroke="#222" stroke-width="1.8"><path d="M18 30s-9-9-9-16a9 9 0 0118 0c0 7-9 16-9 16z"/><circle cx="18" cy="14" r="3"/></svg></div>
  <h3>Local Hampshire Experts</h3><p>Reliable, friendly and community-focused.</p>
</div>
<div class="why-frame"></div>
<div class="placeholder why-photo" role="img" aria-label="Photo of a freshly painted white terraced house front with railings"></div>

<!-- call to action -->
<div class="placeholder cta-bg" role="img" aria-label="Faded photo of a smiling builder in a hard hat"></div>
<div class="cta-box">
  <h2>READY TO START YOUR RENOVATION?</h2>
  <p>Lorem ipsum dolor sit amet, consectetur adipiscing elit, sed do eiusmod tempor incididunt ut labore et dolore magna aliqua. Ut enim ad minim veniam, quis nostrud exercitation ullamco laboris nisi ut aliquip ex ea commodo consequat.</p>
</div>
<div class="cta-circle"><div></div></div>
<a class="skew-btn cta-btn"><span>Get Your Free Quote</span></a>

<!-- before and after -->
<div class="section-mark" style="left:582px;top:3376px"></div>
<h2 class="section-title" style="top:3462px">BEFORE &amp; AFTER</h2>
<div class="placeholder ba-photo" role="img" aria-label="Photo of a finished bathroom with chequered floor" style="left:110px;width:230px;background:linear-gradient(180deg,#d4d7d9,#9a9c9e 70%,#2a2a2a)"></div>
<div class="placeholder ba-photo" role="img" aria-label="Before photo of a terraced house rear, tinted blue" style="left:352px;width:244px;background:linear-gradient(180deg,#5b66b8,#2b3490)"><span class="ba-tag" style="left:18px">Before</span></div>
<div class="placeholder ba-photo" role="img" aria-label="After photo of the renovated terraced house rear, tinted blue" style="left:600px;width:244px;background:linear-gradient(180deg,#7d86c6,#2b3490)"><span class="ba-tag" style="right:18px">After</span></div>
<div class="placeholder ba-photo" role="img" aria-label="Photo of a bathroom during refit with shower screen" style="left:858px;width:230px;background:linear-gradient(180deg,#e1ddd2,#b8a98a)"></div>
<div class="ba-nav prev" style="left:542px"><svg width="24" height="12" viewBox="0 0 24 12"><path d="M23 6H3M8 1L2 6l6 5" stroke="#111" stroke-width="2.4" fill="none"/></svg></div>
<div class="ba-nav next" style="left:602px"><svg width="24" height="12" viewBox="0 0 24 12"><path d="M1 6h20M16 1l6 5-6 5" stroke="#fff" stroke-width="2.4" fill="none"/></svg></div>

<!-- footer -->
<footer class="site-footer" role="img" aria-label="Dark photo of a modern kitchen interior"></footer>
<div class="footer-brand"><div class="brand-mark"></div><div class="brand-name">HARTWELL</div></div>
<nav class="footer-nav"><a href="#">HOME</a><a href="#">ABOUT US</a><a href="#">OUR SERVICES</a><a href="#">WHY CHOOSE US</a></nav>
<div class="socials"><span class="filled"></span><span></span><span></span><span></span></div>
<div class="footer-rule"></div>
<div class="to-top"><svg width="14" height="10" viewBox="0 0 14 10"><path d="M7 1L1 9h12z" fill="#111"/></svg></div>
<div class="copyright">Copyright 2025. Company Name. All Rights Reserved</div>

</body>
</html>
```